Relaunch Instagram Posts Design

We want to give you a better understanding about the expected outcome of this task, and give you a little bit of a background that should help you throughout.
We already have social media accounts, they aren’t active and the posts are outdated. We just finished our rebranding exercise, and accordingly we are planning to have a re-launch where we communicate our new identity, and rebuild our online existence, to enhance our social media presence and engagement.
Thus, we want to formulate the style of posting from the beginning, so that it reflects the identity overall and we can move forward with in a consistent manner.

Find attached details. We will share other files later. You need to read the attachment in the project to understand the requirement. Also, you should use the attached images in the project. You should also use products images from our website...www.bloomvantra.com
Our Primary color is #5725A9, PURPLE (based on color HEX Code)
Our Secondary colors #7C50BE, #A17BD3, #C5A6E8, #EAD1FD
Also, this secondary colors can be used #2B9348, #55A630, #80B918, #AACC00

Target Market(s)

Gift-givers who would like to bring a gift of value and meaning, representing the occasion

Industry/Entity Type

Flowers

Colors

Designer to choose colors to be used in the design.

Requirements
Must have
• Image based posts with little graphics + typography-based posts.... hammer on the emotional aspect, focusing on special moments such as using images related nice moments
Nice to have
• A full overview as in the brief (with all 21 posts), to give the sense of the design direction for us to know if it fits our new brand vision or not.
Should not have
• A typical commercial design direction that focuses so much on direct product communication. This definitely will be there, but we want this to be integrated with the other aspects.

```html
<!DOCTYPE html>
<html lang="en">
<head>
<meta charset="utf-8">
<title>Bloomvantra – Relaunch Posts</title>
<link rel="stylesheet" href="https://fonts.googleapis.com/css2?family=Crimson+Text:ital,wght@0,400;0,600;1,400&family=Kalam:wght@400;700&family=Exo+2:ital,wght@1,800&display=swap">
<style>
  :root{
    --purple:#5725A9;
    --purple-2:#7C50BE;
    --purple-3:#A17BD3;
    --lilac:#C5A6E8;
    --lilac-pale:#EAD1FD;
    --white:#ffffff;
    --board:#1e1e1f;
    --blush:#f6a9bf;
  }
  *{box-sizing:border-box;margin:0;padding:0}
  html,body{width:1200px;height:646px;overflow:hidden;background:var(--board)}
  body{position:relative;font-family:"Crimson Text",Georgia,serif}
  .post{position:absolute;background:var(--white);overflow:hidden;box-shadow:0 6px 16px rgba(0,0,0,.55)}
  .frame{position:absolute;border:2px solid var(--lilac);pointer-events:none;z-index:5}
  .photo,.art{position:absolute}
  .brand{position:absolute;display:flex;align-items:center;gap:5px;color:var(--purple);font-family:"Crimson Text",Georgia,serif;font-weight:400;letter-spacing:1px;line-height:1}
  .brand-dot{width:14px;height:14px;border-radius:50%;background:var(--purple);flex:none}
  .social{position:absolute;display:flex;align-items:center;gap:4px;color:var(--purple);font-family:"Crimson Text",Georgia,serif}
  .social-dot{border-radius:50%;background:var(--purple);flex:none}
  .script{font-family:"Kalam",cursive;font-weight:700}

  /* Hero post */
  .hero{left:65px;top:54px;width:523px;height:524px}
  .hero .frame{left:15px;top:15px;width:493px;height:494px}
  .hero .photo{left:190px;top:0;width:333px;height:318px;background:radial-gradient(circle at 58% 45%,#b52a2e 0 12%,#e9c9b9 30%,#f4e1cc 60%,#ecd3b6 100%)}
  .hero .art{left:38px;top:40px;width:150px;height:278px;background:radial-gradient(ellipse at 45% 30%,#d8cdf2 0 30%,rgba(216,205,242,0) 60%),radial-gradient(ellipse at 40% 70%,#e1d8f5 0 22%,rgba(225,216,245,0) 50%)}
  .order{position:absolute;left:146px;top:106px;width:88px;height:88px;border-radius:50%;background:var(--purple-3);border:3px solid var(--white);color:var(--white);text-align:center;display:flex;flex-direction:column;justify-content:center;line-height:.95;z-index:6}
  .order .o1{font-size:20px;font-weight:600;letter-spacing:.5px}
  .order .o2{font-family:Arial,Helvetica,sans-serif;font-size:23px}
  .hero .band{position:absolute;left:0;top:318px;width:523px;height:139px;background:linear-gradient(90deg,#b296dc 0%,#8a5fc9 30%,#a684d8 65%,#e8dcf6 100%);color:var(--white);text-align:center;z-index:6}
  .hero .band .k1{position:absolute;left:0;right:0;top:8px;font-size:33px;line-height:1}
  .hero .band .k2{position:absolute;left:0;right:0;top:42px;font-size:44px;font-weight:600;line-height:1}
  .hero .band .k3{position:absolute;left:0;right:0;top:91px;font-size:14.5px;line-height:1.25}
  .hero .social{left:252px;top:467px;font-size:13px;gap:7px}
  .hero .social .social-dot{width:20px;height:20px}

  /* Tile: Helping Nature's Beauty */
  .nature{left:617px;top:54px;width:247px;height:247px}
  .nature .frame{left:7px;top:7px;width:233px;height:233px}
  .nature .photo{left:133px;top:0;width:114px;height:247px;background:radial-gradient(circle at 50% 20%,#e4557f 0 18%,transparent 30%),radial-gradient(circle at 40% 60%,#d9456f 0 20%,transparent 32%),linear-gradient(180deg,#8f9a4f,#c24e79 50%,#6c7c3a)}
  .nature .brand{left:24px;top:27px;font-size:9.5px}
  .nature .brand .stack{display:flex;flex-direction:column;gap:1px}
  .nature .panel{position:absolute;left:0;top:74px;width:133px;height:103px;background:linear-gradient(180deg,#8d63cc,#a583d6)}
  .nature .t1{position:absolute;left:30px;top:4px;color:var(--white);font-size:16px;font-weight:400;transform:rotate(-4deg)}
  .nature .t2{position:absolute;left:52px;top:22px;color:var(--white);font-size:18px}
  .nature .t3{position:absolute;left:24px;top:36px;color:var(--white);font-size:30px;line-height:1}
  .nature .t4{position:absolute;left:20px;top:70px;color:var(--white);font-family:"Exo 2",Arial,sans-serif;font-style:italic;font-weight:800;font-size:11px;letter-spacing:.3px}
  .nature .swoosh{position:absolute;left:18px;top:88px}
  .nature .tag{position:absolute;left:24px;top:186px;color:var(--purple-2);font-size:7px;line-height:1.2}
  .nature .social{left:24px;top:217px;font-size:6px}
  .nature .social .social-dot{width:9px;height:9px}

  /* Tile: Fresh Flowers */
  .fresh{left:894px;top:54px;width:247px;height:247px}
  .fresh .frame{left:7px;top:7px;width:233px;height:233px}
  .fresh .photo{left:0;top:29px;width:247px;height:138px;background:radial-gradient(circle at 30% 40%,#c0182a 0 10%,transparent 22%),radial-gradient(circle at 70% 40%,#e98fa9 0 12%,transparent 25%),linear-gradient(135deg,#b31f2d,#eaa6b9 50%,#d4405b)}
  .fresh .panel{position:absolute;left:103px;top:137px;width:124px;height:110px;background:linear-gradient(180deg,#8d63cc,#a98ad9);color:var(--white);z-index:6}
  .fresh .p1{position:absolute;left:14px;top:11px;font-size:13.5px;line-height:1}
  .fresh .p2{position:absolute;left:14px;top:27px;font-size:24px;font-weight:600;line-height:1}
  .fresh .p3{position:absolute;left:14px;top:76px;font-size:6px;line-height:1.25;width:90px}
  .fresh .brand{left:23px;top:182px;font-size:7.5px}
  .fresh .brand .stack{display:flex;flex-direction:column;gap:1px}
  .fresh .brand .brand-dot{width:11px;height:11px}
  .fresh .social{left:22px;top:217px;font-size:6px}
  .fresh .social .social-dot{width:9px;height:9px}

  /* Tile: Flowers for You */
  .foryou{left:617px;top:331px;width:247px;height:247px}
  .foryou .frame{left:7px;top:7px;width:233px;height:233px}
  .foryou .photo-a{left:0;top:0;width:123px;height:124px;background:radial-gradient(circle at 50% 40%,#d5423f 0 14%,#6f8f3d 30%,transparent 45%),linear-gradient(180deg,#9fa7ac,#c7b06d)}
  .foryou .art{left:123px;top:0;width:124px;height:58px;background:radial-gradient(ellipse at 40% 40%,#ddd3f3 0 25%,transparent 55%),radial-gradient(ellipse at 85% 40%,#f7d1d7 0 25%,transparent 55%)}
  .foryou .photo-b{left:123px;top:124px;width:124px;height:123px;background:radial-gradient(circle at 55% 30%,#e14a6d 0 14%,#f3f3f0 30%,transparent 45%),linear-gradient(180deg,#d3d3d3,#c6a27a)}
  .foryou .brand{left:152px;top:67px;font-size:7.5px}
  .foryou .brand .stack{display:flex;flex-direction:column;gap:1px}
  .foryou .brand .brand-dot{width:11px;height:11px}
  .foryou .social{left:147px;top:104px;font-size:6px}
  .foryou .social .social-dot{width:9px;height:9px}
  .foryou .panel{position:absolute;left:0;top:124px;width:123px;height:123px;background:linear-gradient(180deg,#8d63cc,#a583d6);color:var(--white)}
  .foryou .f1{position:absolute;left:18px;top:18px;font-family:"Exo 2",Arial,sans-serif;font-style:italic;font-weight:800;font-size:24px;line-height:1}
  .foryou .f2{position:absolute;left:19px;top:44px;font-family:"Exo 2",Arial,sans-serif;font-style:italic;font-weight:800;font-size:24px;line-height:1}
  .foryou .f3{position:absolute;left:18px;top:78px;font-size:6.5px;line-height:1.3;width:90px}

  /* Tile: Did You Know */
  .know{left:894px;top:331px;width:247px;height:247px;background:linear-gradient(180deg,#8a5fc9,#b9a2e2)}
  .know .frame{left:7px;top:7px;width:233px;height:233px}
  .know .photo{left:0;top:0;width:116px;height:247px;background:radial-gradient(circle at 45% 30%,#d3212f 0 14%,transparent 30%),linear-gradient(180deg,#e9eaee 0 40%,#b9d9ef 70%,#e8e8ea)}
  .know .art-top{left:188px;top:0;width:59px;height:70px;background:radial-gradient(circle at 70% 35%,var(--blush) 0 35%,transparent 70%)}
  .know .art-bottom{left:80px;top:200px;width:60px;height:47px;background:radial-gradient(circle at 50% 55%,var(--blush) 0 35%,transparent 70%);z-index:6}
  .know .d1{position:absolute;left:138px;top:36px;color:var(--white);font-size:22px;line-height:1}
  .know .d2{position:absolute;left:143px;top:56px;color:var(--white);font-size:30px;line-height:1.1}
  .know .d3{position:absolute;left:138px;top:97px;color:var(--white);font-size:22px;line-height:1}
  .know .facts{position:absolute;left:126px;top:123px;width:118px;list-style:none;color:var(--white);font-size:7.5px;line-height:12.7px}
  .know .facts li{position:relative;padding-left:11px}
  .know .facts li::before{content:"-";position:absolute;left:0}
</style>
</head>
<body>

<section class="post hero">
  <div class="art" role="img" aria-label="Line illustration of lavender blossoms with golden stems"></div>
  <div class="photo" role="img" aria-label="Photo of a bouquet of red roses and dried flowers wrapped in white and kraft paper"></div>
  <div class="order"><span class="o1">ORDER</span><span class="o2">NOW!</span></div>
  <div class="band">
    <p class="k1">High Quality &amp;</p>
    <p class="k2">Fresh Flowers</p>
    <p class="k3">Lorem ipsum dolor sit amet, consectetuer<br>adipiscing elit, sed diam.</p>
  </div>
  <div class="social"><span class="social-dot"></span><span>@username</span></div>
  <div class="frame"></div>
</section>

<section class="post nature">
  <div class="brand"><span class="stack"><span>BLOOM</span><span>VANTRA</span></span><span class="brand-dot"></span></div>
  <div class="panel">
    <span class="t1 script">Helping</span>
    <span class="t2 script">Nature's</span>
    <span class="t3 script">Beauty</span>
    <span class="t4">Last Forever</span>
    <svg class="swoosh" width="106" height="8" viewBox="0 0 106 8"><path d="M2 6 Q50 1 104 2" stroke="#fff" stroke-width="2" fill="none" stroke-linecap="round"/></svg>
  </div>
  <p class="tag">Fresh flowers &amp;<br>gifts for all occasions</p>
  <div class="social"><span class="social-dot"></span><span>@username</span></div>
  <div class="photo" role="img" aria-label="Close-up photo of pink roses with pearls and feathers"></div>
  <div class="frame"></div>
</section>

<section class="post fresh">
  <div class="photo" role="img" aria-label="Photo of a mixed bouquet of red, pink and cream roses"></div>
  <div class="brand"><span class="stack"><span>BLOOM</span><span>VANTRA</span></span><span class="brand-dot"></span></div>
  <div class="social"><span class="social-dot"></span><span>@username</span></div>
  <div class="frame"></div>
  <div class="panel">
    <p class="p1">High Quality &amp;</p>
    <p class="p2">Fresh<br>Flowers</p>
    <p class="p3">Lorem ipsum dolor sit amet, consectetuer adipiscing elit, sed diam.</p>
  </div>
</section>

<section class="post foryou">
  <div class="photo photo-a" role="img" aria-label="Photo of a colourful flower arrangement in a gold gift box"></div>
  <div class="art" role="img" aria-label="Illustration of lavender blossoms and green leaves"></div>
  <div class="brand"><span class="stack"><span>BLOOM</span><span>VANTRA</span></span><span class="brand-dot"></span></div>
  <div class="social"><span class="social-dot"></span><span>@username</span></div>
  <div class="panel">
    <p class="f1">Flowers</p>
    <p class="f2">for You</p>
    <p class="f3">Lorem ipsum dolor sit amet, consectetuer adipiscing elit, sed diam.</p>
  </div>
  <div class="photo photo-b" role="img" aria-label="Photo of pink and white flowers in a vase beside a wrapped gift"></div>
  <div class="frame"></div>
</section>

<section class="post know">
  <div class="photo" role="img" aria-label="Photo of a red rose bouquet with chocolates in blue wrapping"></div>
  <div class="art art-top" role="img" aria-label="Illustration of a pink blossom"></div>
  <div class="art art-bottom" role="img" aria-label="Illustration of a pink blossom"></div>
  <p class="d1">DID</p>
  <p class="d2 script">You</p>
  <p class="d3">KNOW?</p>
  <ul class="facts">
    <li>Lorem ipsum dolor sit amet, consectetuer adipiscing elit.</li>
    <li>Sed diam nonummy nibh euismod tincidunt ut lao-reet dolore magna aliquam erat volutpat.</li>
  </ul>
  <div class="frame"></div>
</section>

</body>
</html>
```